Brannigan Ashcroft LLC. custom built/handcrafted

I am recent small business owner looking to sell my art(drawings) and woodworking projects from my home. I have a very rough draft of a simple card design created on a simple digital program. I was hoping for a fancier lettering on the initial letters (BA). More of a calligraphy style. Also, the yellow border around the logo I would like to be a gold foil look. For it to be shiny or reflective look and to keep the other letters black with a consistent font on the card and the card white.

Target Market(s)

Local and neighboring cities

Industry/Entity Type

Art (drawing)/Woodworking

Contact Information for Business Card

My email tpashcroft@mailvane.net, phone number 949-517-3068. In the files provided it has a yellow border around the logo and I was looking to make that a gold foil.

Font styles to use
Serif
Decorative
Script

Requirements
Nice to have
• symbols for having a Facebook and Instagram

```html
<!DOCTYPE html>
<html lang="en">
<head>
<meta charset="utf-8">
<title>Brannigan Ashcroft LLC. Business Card</title>
<link rel="stylesheet" href="https://fonts.googleapis.com/css2?family=Poppins:wght@300;400;600;700&display=swap">
<style>
  :root {
    --backdrop: #d4d4d6;
    --card-white: #fbfbfa;
    --ink: #2a2a2a;
    --ink-soft: #555555;
    --wood-dark: #1e1814;
    --wood-mid: #3a2e27;
    --gold-deep: #c4561a;
    --gold-mid: #e39a16;
    --gold-light: #f2d22a;
    --logo-white: #f1f1f1;
  }
  * { margin: 0; padding: 0; box-sizing: border-box; }
  html, body { width: 1200px; height: 900px; overflow: hidden; }
  body {
    background: var(--backdrop);
    font-family: "Poppins", sans-serif;
    display: flex;
    flex-direction: column;
    align-items: center;
    justify-content: center;
    gap: 56px;
  }
  .card {
    width: 560px;
    height: 320px;
    position: relative;
    box-shadow: 0 10px 24px rgba(0,0,0,0.18);
  }
  /* Front */
  .card-front {
    background: var(--card-white);
    color: var(--ink);
    display: flex;
    flex-direction: column;
    align-items: center;
    padding-top: 62px;
    text-align: center;
  }
  .owner-name { font-weight: 700; font-size: 27px; letter-spacing: 0.2px; line-height: 1.1; }
  .owner-title { font-weight: 300; font-size: 13px; letter-spacing: 1.5px; color: var(--ink-soft); margin-top: 2px; }
  .contact-divider {
    display: flex; align-items: center; gap: 8px; margin-top: 20px;
  }
  .divider-rule { width: 62px; height: 1px; background: var(--ink); }
  .contact-icon {
    width: 24px; height: 24px; border-radius: 50%; background: var(--ink);
    display: flex; align-items: center; justify-content: center;
  }
  .contact-lines { margin-top: 12px; font-size: 16px; font-weight: 400; line-height: 1.3; letter-spacing: 0.6px; }
  .social-row { display: flex; gap: 6px; margin-top: 12px; }
  .social-dot { width: 22px; height: 22px; border-radius: 50%; background: var(--ink); }
  /* Back */
  .card-back { overflow: hidden; }
  .wood-surface {
    position: absolute; inset: 0;
    background: linear-gradient(100deg, var(--wood-dark) 0%, var(--wood-mid) 35%, #2a211c 60%, var(--wood-mid) 85%, var(--wood-dark) 100%);
  }
  .gold-frame { position: absolute; inset: 0; }
  .brand-lockup {
    position: absolute; inset: 0;
    display: flex; flex-direction: column; align-items: center; justify-content: center;
  }
  .brand-initials {
    font-weight: 600; font-size: 96px; line-height: 1; color: var(--logo-white); letter-spacing: 4px;
  }
  .brand-name {
    font-weight: 400; font-size: 19px; letter-spacing: 1px; color: var(--gold-mid); margin-top: 6px;
  }
</style>
</head>
<body>
  <section class="card card-front">
    <h1 class="owner-name">Tobias P. Ashcroft</h1>
    <p class="owner-title">OWNER</p>
    <div class="contact-divider">
      <span class="divider-rule"></span>
      <span class="contact-icon" aria-label="Phone">
        <svg width="13" height="13" viewBox="0 0 24 24"><path fill="#fff" d="M6.6 10.8a15.1 15.1 0 0 0 6.6 6.6l2.2-2.2a1 1 0 0 1 1-.25 11.4 11.4 0 0 0 3.6.57 1 1 0 0 1 1 1V20a1 1 0 0 1-1 1A17 17 0 0 1 3 4a1 1 0 0 1 1-1h3.5a1 1 0 0 1 1 1c0 1.25.2 2.45.57 3.57a1 1 0 0 1-.25 1z"/></svg>
      </span>
      <span class="contact-icon" aria-label="Email">
        <svg width="13" height="13" viewBox="0 0 24 24"><path fill="#fff" d="M3 5h18v14H3z"/><path fill="none" stroke="#2a2a2a" stroke-width="2" d="M3 6l9 7 9-7"/></svg>
      </span>
      <span class="divider-rule"></span>
    </div>
    <div class="contact-lines">
      <p class="contact-phone">949-517-3068</p>
      <p class="contact-email">tpashcroft@mailvane.net</p>
    </div>
    <div class="social-row">
      <span class="social-dot"></span>
      <span class="social-dot"></span>
    </div>
  </section>

  <section class="card card-back">
    <div class="wood-surface" role="img" aria-label="Dark stained wood grain texture"></div>
    <svg class="gold-frame" width="560" height="320" viewBox="0 0 560 320">
      <defs>
        <linearGradient id="goldFoil" x1="0" y1="1" x2="1" y2="0">
          <stop offset="0" stop-color="var(--gold-deep)"/>
          <stop offset="0.5" stop-color="var(--gold-mid)"/>
          <stop offset="1" stop-color="var(--gold-light)"/>
        </linearGradient>
      </defs>
      <rect x="80" y="52" width="400" height="216" fill="none" stroke="url(#goldFoil)" stroke-width="3"/>
    </svg>
    <div class="brand-lockup">
      <div class="brand-initials">BA</div>
      <div class="brand-name">BRANNIGAN ASHCROFT</div>
    </div>
  </section>
</body>
</html>
```